School Management website

I need page design for our school management system website

Base website is www.brindavo.com. When the student logs in, he will reach the below pages.
You can either design with white and blue background or grey and white background

Page 1 - School Info

Header
product name("Brindavo") in left corner
logout link in right corner

LeftMenu

Dashboard
School Info
School Settings
Staffs
Classes
Messaging
Contact Us

Footer
About link and copyright text

School Info content
The page should have breadcrumb

The content of this page will be the school profile
We have to show the school logo
Name
School Type
School Code
School Count
School Address
School phone 1&2
School Email
School Website

The page content should show edit school profile link which will take the user to another page

```html
<!DOCTYPE html>
<html lang="en">
<head>
<meta charset="utf-8">
<title>Brindavo – School Info</title>
<link href="https://fonts.googleapis.com/css2?family=Roboto:wght@300;400;500;700&family=Open+Sans:wght@400&family=Tinos&display=swap" rel="stylesheet">
<style>
  :root {
    --header-bg: #f4f3f3;
    --line: #dcdcdc;
    --menu-bg: #e8e8e8;
    --menu-text: #6a6a6a;
    --brand-blue: #2aa3e6;
    --blue: #3a8fdc;
    --blue-soft: #c5d9ec;
    --blue-ink: #3a6fa8;
    --purple: #9339dc;
    --purple-soft: #dcc8ec;
    --purple-ink: #8b5ab8;
    --lime: #d9dc37;
    --lime-soft: #e7e8b8;
    --lime-ink: #8c8e2a;
    --orange: #dc6a39;
    --orange-soft: #eccbbf;
    --orange-ink: #b8563a;
    --green: #c0dc39;
    --green-soft: #dfe8b9;
    --green-ink: #7f9228;
    --amber: #dc9a39;
    --amber-soft: #ecd7c0;
    --amber-ink: #a8702a;
    --charcoal: #545454;
    --charcoal-soft: #cfcfcf;
    --charcoal-ink: #444;
    --pink: #dc39c5;
    --pink-soft: #ebc8e8;
    --pink-ink: #a83a98;
    --footer-bg: #484646;
    --footer-text: #a9a7a7;
    --white: #ffffff;
  }
  * { box-sizing: border-box; margin: 0; padding: 0; }
  html, body { width: 1070px; height: 1200px; overflow: hidden; background: var(--white); }
  body { font-family: "Roboto", Arial, sans-serif; }
  .page {
    position: relative; width: 1000px; height: 1122px;
    transform: scale(1.07); transform-origin: 0 0; background: var(--white);
  }

  /* Header */
  .site-header {
    position: absolute; left: 0; top: 0; width: 1000px; height: 98px;
    background: var(--header-bg); border-bottom: 1px solid var(--line);
  }
  .brand { position: absolute; left: 42px; top: 40px; display: flex; align-items: center; gap: 8px; }
  .brand-mark { width: 14px; height: 14px; background: var(--brand-blue); }
  .brand-name { font-size: 26px; font-weight: 700; color: var(--brand-blue); letter-spacing: -0.5px; }
  .logout { position: absolute; left: 811px; top: 54px; font-size: 13px; color: #777; text-decoration: none; }

  /* Side menu */
  .side-menu { position: absolute; left: 0; top: 98px; width: 196px; height: 802px; background: var(--menu-bg); border-right: 1px solid #d0d0d0; }
  .side-menu ul { list-style: none; }
  .menu-item {
    height: 70px; display: flex; align-items: center; padding-left: 56px;
    font-size: 16px; font-weight: 300; color: var(--menu-text);
    border-bottom: 5px solid var(--line);
  }
  .menu-item.first { height: 73px; }
  .menu-item.active { background: var(--white); margin-right: -1px; }

  /* School banner */
  .school-banner { position: absolute; left: 235px; top: 142px; width: 444px; height: 123px; border: 1px solid #dcdcdc; display: flex; }
  .banner-label {
    width: 111px; background: var(--blue); color: var(--white); font-size: 14px;
    display: flex; align-items: center; justify-content: center; text-align: center; line-height: 18px;
    margin: -1px 0 -1px -1px;
  }
  .banner-logo { flex: 1; display: flex; align-items: center; justify-content: center; gap: 12px; }
  .banner-logo .mark { width: 18px; height: 18px; background: var(--blue); }
  .banner-logo .name { font-size: 20px; font-weight: 400; color: var(--blue); }

  /* Profile cards */
  .card { position: absolute; width: 176px; height: 165px; }
  .card-head { height: 35px; display: flex; align-items: center; justify-content: space-between; padding: 0 9px 0 8px; font-size: 13px; }
  .card-body { height: 130px; display: flex; align-items: center; justify-content: center; text-align: center; color: var(--white); }
  .edit-btn {
    display: flex; align-items: center; gap: 6px; height: 22px; padding: 0 8px 0 9px;
    border: 1px solid currentColor; font-size: 13px; opacity: .85; background: rgba(255,255,255,.25);
  }
  .value-md { font-size: 18px; line-height: 22px; }
  .value-lg { font-size: 20px; }
  .value-xl { font-size: 34px; }
  .value-sm { font-size: 17px; line-height: 22px; }

  .card.name .card-head { background: var(--blue-soft); color: var(--blue-ink); }
  .card.name .card-body { background: var(--blue); }
  .card.type .card-head { background: var(--purple-soft); color: var(--purple-ink); }
  .card.type .card-body { background: var(--purple); }
  .card.code .card-head { background: var(--lime-soft); color: var(--lime-ink); }
  .card.code .card-body { background: var(--lime); }
  .card.count .card-head { background: var(--orange-soft); color: var(--orange-ink); }
  .card.count .card-body { background: var(--orange); }
  .card.address .card-head { background: var(--green-soft); color: var(--green-ink); }
  .card.address .card-body { background: var(--green); }
  .card.phone .card-head { background: var(--amber-soft); color: var(--amber-ink); }
  .card.phone .card-body { background: var(--amber); }
  .card.email .card-head { background: var(--charcoal-soft); color: var(--charcoal-ink); }
  .card.email .card-body { background: var(--charcoal); }
  .card.website .card-head { background: var(--pink-soft); color: var(--pink-ink); }
  .card.website .card-body { background: var(--pink); }

  /* Footer */
  .site-footer { position: absolute; left: 0; top: 900px; width: 1000px; height: 222px; background: var(--footer-bg); }
  .footer-col { position: absolute; top: 41px; width: 203px; }
  .footer-title { display: flex; align-items: center; gap: 10px; font-size: 12px; font-weight: 700; color: var(--white); height: 16px; }
  .footer-title::after { content: ""; flex: 1; height: 1px; background: #6a6868; }
  .footer-text { font-family: "Open Sans", Arial, sans-serif; font-size: 10.5px; line-height: 16px; color: var(--footer-text); margin-top: 22px; }
  .subscribe { display: flex; margin-top: 22px; }
  .subscribe .field { width: 146px; height: 24px; background: #3a3939; font-family: "Tinos", serif; font-size: 10px; color: #777; padding: 6px 7px; }
  .subscribe .send { width: 57px; height: 24px; background: var(--brand-blue); color: var(--white); font-family: "Tinos", serif; font-size: 11px; display: flex; align-items: center; justify-content: center; }
  .contact-row { display: flex; gap: 8px; font-family: "Open Sans", Arial, sans-serif; font-size: 10.5px; line-height: 15px; color: var(--footer-text); }
  .contact-row svg { flex: none; margin-top: 2px; }
  .contact-divider { height: 1px; background: #2f76b0; margin: 9px 0 10px; }
  .footer-links { list-style: none; margin-top: 22px; }
  .footer-links li { font-family: "Tinos", serif; font-size: 13px; color: #9a9898; height: 28px; }
</style>
</head>
<body>
<div class="page">

  <header class="site-header">
    <div class="brand"><span class="brand-mark"></span><span class="brand-name">Brindavo</span></div>
    <a class="logout" href="#">Logout</a>
  </header>

  <nav class="side-menu">
    <ul>
      <li class="menu-item first">Dashboard</li>
      <li class="menu-item active">School Info</li>
      <li class="menu-item">School Settings</li>
      <li class="menu-item">Staffs</li>
      <li class="menu-item">Classes</li>
      <li class="menu-item">Messaging</li>
      <li class="menu-item">Contact Us</li>
    </ul>
  </nav>

  <section class="school-banner">
    <div class="banner-label">SCHOOL<br>NAME</div>
    <div class="banner-logo"><span class="mark"></span><span class="name">The Bright Acorn Academy</span></div>
  </section>

  <svg width="0" height="0" style="position:absolute">
    <defs>
      <symbol id="icon-edit" viewBox="0 0 12 12">
        <path d="M1 2.5h5M1 2.5v8.5h8.5v-5" fill="none" stroke="currentColor" stroke-width="1.4"/>
        <path d="M5 7l5.5-5.5" stroke="currentColor" stroke-width="1.6"/>
      </symbol>
    </defs>
  </svg>

  <article class="card name" style="left:235px;top:343px">
    <div class="card-head"><span>Name</span><span class="edit-btn"><svg width="11" height="11"><use href="#icon-edit"/></svg>Edit</span></div>
    <div class="card-body value-md">The Bright Acorn<br>Academy</div>
  </article>
  <article class="card type" style="left:427px;top:343px">
    <div class="card-head"><span>School Type</span><span class="edit-btn"><svg width="11" height="11"><use href="#icon-edit"/></svg>Edit</span></div>
    <div class="card-body value-lg">The Bright</div>
  </article>
  <article class="card code" style="left:607px;top:343px">
    <div class="card-head"><span>School Code</span><span class="edit-btn"><svg width="11" height="11"><use href="#icon-edit"/></svg>Edit</span></div>
    <div class="card-body value-xl">ER0876</div>
  </article>
  <article class="card count" style="left:798px;top:343px">
    <div class="card-head"><span>School Count</span><span class="edit-btn"><svg width="11" height="11"><use href="#icon-edit"/></svg>Edit</span></div>
    <div class="card-body value-xl">0456</div>
  </article>

  <article class="card address" style="left:235px;top:523px">
    <div class="card-head"><span>School Address</span><span class="edit-btn"><svg width="11" height="11"><use href="#icon-edit"/></svg>Edit</span></div>
    <div class="card-body value-md">414 Maple Row<br>Eastfield,<br>NY 10044-2210</div>
  </article>
  <article class="card phone" style="left:427px;top:523px">
    <div class="card-head"><span>School phone</span><span class="edit-btn"><svg width="11" height="11"><use href="#icon-edit"/></svg>Edit</span></div>
    <div class="card-body value-md" style="line-height:31px">021 555 0143<br>021 555 0144</div>
  </article>
  <article class="card email" style="left:607px;top:523px">
    <div class="card-head"><span>School Email</span><span class="edit-btn"><svg width="11" height="11"><use href="#icon-edit"/></svg>Edit</span></div>
    <div class="card-body value-sm">brightacorn<br>@mailbox.com</div>
  </article>
  <article class="card website" style="left:798px;top:523px">
    <div class="card-head"><span>School Website</span><span class="edit-btn"><svg width="11" height="11"><use href="#icon-edit"/></svg>Edit</span></div>
    <div class="card-body value-sm">TheBright<br>Acorn .com</div>
  </article>

  <footer class="site-footer">
    <div class="footer-col" style="left:45px">
      <div class="footer-title">About Brindavo</div>
      <p class="footer-text">To know more about us, send your email id. We will contact you back</p>
      <div class="subscribe"><span class="field">Email goes here...</span><span class="send">Send</span></div>
    </div>
    <div class="footer-col" style="left:265px">
      <div class="footer-title">Contact Info</div>
      <div class="contact-row" style="margin-top:22px">
        <svg width="10" height="10" viewBox="0 0 10 10"><path d="M2 0.5l2 2-1 1.2c.6 1.3 1.6 2.3 2.9 2.9l1.2-1 2 2-1.3 1.6C4.3 9 1 5.7.5 1.8z" fill="#2aa3e6"/></svg>
        <div>Phone:<br>+91 90000 12345</div>
      </div>
      <div class="contact-divider"></div>
      <div class="contact-row">
        <svg width="10" height="10" viewBox="0 0 10 10"><circle cx="5" cy="5" r="4.5" fill="#2aa3e6"/><path d="M1 5h8M5 .5c-2 2.5-2 6.5 0 9M5 .5c2 2.5 2 6.5 0 9" fill="none" stroke="#484646" stroke-width=".8"/></svg>
        <div>E-mail:<br>contact@brindavo.com</div>
      </div>
    </div>
    <div class="footer-col" style="left:485px">
      <div class="footer-title">Get in touch</div>
      <ul class="footer-links"><li>Contact Us</li><li>Partner with us</li></ul>
    </div>
    <div class="footer-col" style="left:705px">
      <div class="footer-title">Connect with us</div>
      <ul class="footer-links"><li>Chirpline</li><li>Friendhub</li><li>Circles +</li><li>Worknet</li></ul>
    </div>
  </footer>

</div>
</body>
</html>
```